Songs Cover Art. Song tittle DJ K - Keep The Floor Lit

Hey

I need a cover art for my songs. My genre is Big Room House/EDM music and my DJ name is DJ K. Song title is Keep The Floor Lit. I'm a producer and i need a designer to design all my cover art so that i will be able upload my song with a cover art. Do let me know if you have any questions.

Song Tittle: Keep The Floor Lit
Artist name: DJ K

Thanks

Industry/Entity Type

House

Requirements
Should not have
• Please dont make the design to colourful.

```html
<!DOCTYPE html>
<html lang="en">
<head>
<meta charset="utf-8">
<title>DJ K – Keep The Floor Lit</title>
<link rel="stylesheet" href="https://fonts.googleapis.com/css2?family=Righteous&family=Lexend:wght@600&display=swap">
<style>
  :root {
    --space-deep: #0f0d0e;
    --space-mid: #1f1c1d;
    --ornament-tone: #3a3637;
    --ink: #ffffff;
  }
  html, body {
    margin: 0;
    padding: 0;
    width: 1200px;
    height: 1200px;
    overflow: hidden;
    background: var(--space-deep);
  }
  .cover {
    position: relative;
    width: 1200px;
    height: 1200px;
  }
  .cover__sky {
    position: absolute;
    inset: 0;
    background: radial-gradient(ellipse at 50% 45%, var(--space-mid) 0%, #171415 55%, var(--space-deep) 100%);
  }
  .cover__art {
    position: absolute;
    inset: 0;
  }
  .title {
    font-family: "Righteous", sans-serif;
    fill: var(--ink);
    font-size: 156px;
  }
  .artist {
    font-family: "Lexend", sans-serif;
    font-weight: 600;
    fill: var(--ink);
    font-size: 50px;
    letter-spacing: 22px;
  }
  .ornament-slot {
    fill: var(--ornament-tone);
  }
</style>
</head>
<body>
  <main class="cover">
    <div class="cover__sky" role="img" aria-label="Dark night sky scattered with small faint stars"></div>
    <svg class="cover__art" width="1200" height="1200" viewBox="0 0 1200 1200" xmlns="http://www.w3.org/2000/svg">
      <text class="title" x="94" y="600" textLength="914" lengthAdjust="spacingAndGlyphs">KEEP THE</text>
      <rect class="ornament-slot" x="1026" y="526" width="120" height="44" rx="4"
            role="img" aria-label="Small white left-pointing chevron ornament"/>

      <rect class="ornament-slot" x="56" y="666" width="118" height="44" rx="4"
            role="img" aria-label="Small white right-pointing chevron ornament"/>
      <text class="title" x="216" y="756" textLength="884" lengthAdjust="spacingAndGlyphs">FLOOR LIT</text>

      <text class="artist" x="611" y="1188" text-anchor="middle">DJ K</text>
    </svg>
  </main>
</body>
</html>
```